Northern Guild of Acute Care Doctors Membership Poster Design

We need a poster that highlights why physicians should become a member of our association.

As the national voice of emergency medicine (EM), NGAD provides continuing medical education, advocates on behalf of emergency physicians and their patients, supports research and strengthens the EM community. In co-operation with other specialties and committees, NGAD also plays a vital role in the development of national standards and clinical guidelines.

NGAD keeps Canadian emergency physicians informed of developments in the clinical practice of EM and addresses political and societal changes, that affect the delivery of emergency health care.

Vision
Leading excellence in Emergency Medicine across Canada

Mission
NGAD champions excellence in Emergency Medicine in Canada by:

Advocating for Emergency Physicians and their patients;
Connecting Emergency Physicians;
Leading Emergency Medicine education;
Fostering research and innovation
Defining standards for quality Emergency Care
Collaborating with Emergency Care providers.

Target Market(s)

Physicians, Residents and Medical Students

Industry/Entity Type

Doctor

Font styles to use
Sans Serif

Requirements
Must have
• Why belong?
• Career Development
• Vision
• Leading excellence in Emergency Medicine across Canada
• Mission
• NGAD champions excellence in Emergency Medicine in Canada by:
• Advocating for Emergency Physicians and their patients;
• Connecting Emergency Physicians;
• Leading Emergency Medicine education;
• Fostering research and innovation
• Defining standards for quality Emergency Care
• Collaborating with Emergency Care providers.
• Financial Discounts
• Special rates at Brellwick Inns
• Discount on fares from Trelo Trains
• Discounts on home and auto insurance thought the Halvesta Group and Prudora Choice
• Special rates on medical and dental insurance through Bluefen Cover Canada
• Special rates with Kestrin Mobile or Vomba
• Discounts on tickets from Olstander Stageworks
• Discounts on tickets from Marquee Tours Nationwide
• Advocacy
• NGAD advocates on behalf of you and your patients
• We support the development of the specialty of emergency medicine for you
• Gain a larger voice representing you and your specialty
• Networking Opportunities
• Opportunity to become involved with NGAD committees and sections
• Connect with colleagues and potential mentors at events and through online discussions
• Member Types
• Physician Members
• Resident Members
• Student Members
• Associate Members
• ngad-example.ca
• Corporate colours or colours that are complimentary to our corporate colours
• Hex 0077b2
• Hex DF0631
Nice to have
• Pictures

```html
<!DOCTYPE html>
<html lang="en">
<head>
<meta charset="utf-8">
<title>NGAD Membership Poster</title>
<link href="https://fonts.googleapis.com/css2?family=Oswald:wght@500;700&family=Roboto+Condensed:wght@400;700&family=Roboto:wght@400;700&display=swap" rel="stylesheet">
<style>
  :root {
    --blue: #0077b2;
    --blue-deep: #005d8f;
    --red: #df0631;
    --white: #ffffff;
    --ink: #1d2a36;
    --grey: #e9edf0;
  }
  * { margin: 0; padding: 0; box-sizing: border-box; }
  html, body { width: 727px; height: 1200px; overflow: hidden; background: var(--white); }
  .poster {
    position: relative; width: 727px; height: 1200px; overflow: hidden;
    font-family: "Roboto", Arial, sans-serif; color: var(--ink);
  }
  .backdrop { position: absolute; inset: 0; }
  .hero-photo { position: absolute; left: 170px; top: 0; width: 557px; height: 370px; }
  .brand { position: absolute; left: 28px; top: 34px; }
  .brand-name {
    display: flex; align-items: center; gap: 10px;
    font-family: "Roboto Condensed", sans-serif; font-weight: 700; font-size: 30px; color: var(--blue);
  }
  .brand-name .mark { width: 18px; height: 18px; background: var(--red); }
  .brand-years { font-family: "Roboto Condensed", sans-serif; font-weight: 700; font-size: 22px; color: var(--blue); margin-top: 62px; }
  .site { font-family: "Oswald", sans-serif; font-weight: 700; font-size: 34px; color: var(--blue); margin-top: 6px; letter-spacing: 0.5px; }
  .inset-photo { position: absolute; left: 470px; top: 226px; width: 176px; height: 176px; }
  .headline { position: absolute; left: 32px; top: 348px; color: var(--white); }
  .headline h1 {
    font-family: "Oswald", sans-serif; font-weight: 700; font-size: 74px;
    line-height: 74px; letter-spacing: 1px; white-space: nowrap;
  }
  .headline h2 {
    position: absolute; left: 300px; top: 100px; white-space: nowrap;
    font-family: "Oswald", sans-serif; font-weight: 500; font-size: 34px; line-height: 40px; text-transform: uppercase;
  }
  .tab {
    display: block; background: var(--red); color: var(--white);
    font-family: "Roboto Condensed", sans-serif; font-weight: 700; font-size: 16px;
    text-transform: uppercase; padding: 5px 14px 4px; letter-spacing: 0.5px;
    clip-path: polygon(0 0, 100% 0, 94% 100%, 0 100%);
  }
  .block { position: absolute; }
  .on-blue { color: var(--white); }
  .lead { font-weight: 700; font-size: 14px; line-height: 1.3; margin: 8px 0 0 6px; }
  .list { list-style: none; margin: 9px 0 0 6px; font-size: 14px; line-height: 1.25; }
  .list li { position: relative; padding-left: 16px; margin-bottom: 8px; }
  .list li::before { content: ""; position: absolute; left: 0; top: 5px; width: 7px; height: 7px; background: currentColor; }
  .list.sub li { padding-left: 28px; margin-bottom: 4px; }
  .list.sub li::before { left: 12px; }
  .list.sub li.head { padding-left: 16px; font-weight: 700; margin-bottom: 6px; }
  .list.sub li.head::before { left: 0; }
  .on-white .list { color: var(--blue-deep); }
  .vision { left: 30px; top: 512px; width: 320px; }
  .mission { left: 30px; top: 592px; width: 330px; }
  .finance { left: 380px; top: 560px; width: 320px; }
  .advocacy { left: 30px; top: 962px; width: 320px; }
  .network { left: 380px; top: 962px; width: 320px; }
  .members {
    position: absolute; left: 12px; right: 12px; top: 1142px; height: 38px;
    background: var(--blue); display: flex; align-items: center; justify-content: space-between;
    padding-right: 12px; white-space: nowrap;
    font-family: "Roboto Condensed", sans-serif; font-weight: 700; font-size: 13px;
    color: var(--white); text-transform: uppercase;
  }
  .members .label { background: var(--red); height: 100%; display: flex; align-items: center; padding: 0 12px; }
  .members .type { display: flex; align-items: center; gap: 6px; }
  .members .type::before { content: ""; width: 6px; height: 6px; background: var(--white); }
</style>
</head>
<body>
<div class="poster">
  <svg class="backdrop" width="727" height="1200" viewBox="0 0 727 1200" aria-hidden="true">
    <rect x="0" y="0" width="727" height="1200" fill="#ffffff"/>
    <rect x="0" y="1130" width="727" height="70" fill="#e9edf0"/>
  </svg>

  <svg class="hero-photo" viewBox="0 0 557 370" role="img" aria-label="Photograph of emergency physicians in scrubs attending to a patient">
    <defs>
      <linearGradient id="heroTone" x1="0" y1="0" x2="1" y2="1">
        <stop offset="0" stop-color="#eef2f5"/>
        <stop offset="0.55" stop-color="#a9bccb"/>
        <stop offset="1" stop-color="#6f8aa0"/>
      </linearGradient>
    </defs>
    <polygon points="0,0 557,0 557,362 0,330" fill="url(#heroTone)"/>
  </svg>

  <svg class="backdrop" width="727" height="1200" viewBox="0 0 727 1200" aria-hidden="true">
    <polygon points="0,312 727,356 727,374 0,330" fill="#df0631"/>
    <polygon points="0,336 727,380 727,890 363,926 0,890" fill="#0077b2"/>
    <polygon points="0,898 363,934 727,898 727,912 363,948 0,912" fill="#df0631"/>
  </svg>

  <div class="brand">
    <div class="brand-name"><span class="mark"></span>NGAD</div>
    <div class="brand-years">1978–2018</div>
    <div class="site">NGAD-EXAMPLE.CA</div>
  </div>

  <svg class="inset-photo" viewBox="0 0 180 180" role="img" aria-label="Photograph of a care team working at a bedside">
    <defs>
      <radialGradient id="insetTone" cx="0.5" cy="0.45" r="0.6">
        <stop offset="0" stop-color="#8fa6b8"/>
        <stop offset="1" stop-color="#3f5a70"/>
      </radialGradient>
    </defs>
    <circle cx="90" cy="90" r="86" fill="url(#insetTone)" stroke="#ffffff" stroke-width="6"/>
  </svg>

  <div class="headline">
    <h1>WHY<br>BELONG?</h1>
    <h2>Career Development</h2>
  </div>

  <section class="block vision on-blue">
    <span class="tab">Vision</span>
    <p class="lead">Leading excellence in Emergency Medicine across Canada</p>
  </section>

  <section class="block mission on-blue">
    <span class="tab">Mission</span>
    <ul class="list sub">
      <li class="head">NGAD champions excellence in Emergency Medicine in Canada by:</li>
      <li>Advocating for Emergency Physicians and their patients;</li>
      <li>Connecting Emergency Physicians;</li>
      <li>Leading Emergency Medicine education;</li>
      <li>Fostering research and innovation</li>
      <li>Defining standards for quality Emergency Care</li>
      <li>Collaborating with Emergency Care providers.</li>
    </ul>
  </section>

  <section class="block finance on-blue">
    <span class="tab">Financial Discounts</span>
    <ul class="list">
      <li>Special rates at Brellwick Inns</li>
      <li>Discount on fares from Trelo Trains</li>
      <li>Discounts on home and auto insurance thought the Halvesta Group and Prudora Choice</li>
      <li>Special rates on medical and dental insurance through Bluefen Cover Canada</li>
      <li>Special rates with Kestrin Mobile or Vomba</li>
      <li>Discounts on tickets from Olstander Stageworks</li>
      <li>Discounts on tickets from Marquee Tours Nationwide</li>
    </ul>
  </section>

  <section class="block advocacy on-white">
    <span class="tab">Advocacy</span>
    <ul class="list">
      <li>NGAD advocates on behalf of you and your patients</li>
      <li>We support the development of the specialty of emergency medicine for you</li>
      <li>Gain a larger voice representing you and your specialty</li>
    </ul>
  </section>

  <section class="block network on-white">
    <span class="tab">Networking Opportunities</span>
    <ul class="list">
      <li>Opportunity to become involved with NGAD committees and sections</li>
      <li>Connect with colleagues and potential mentors at events and through online discussions</li>
    </ul>
  </section>

  <div class="members">
    <span class="label">Member Types:</span>
    <span class="type">Physician Members</span>
    <span class="type">Resident Members</span>
    <span class="type">Student Members</span>
    <span class="type">Associate Members</span>
  </div>
</div>
</body>
</html>
```